E-Book-Cover-Design im Stil eines magischen Buches gesucht
Zielgruppe
Zielgruppe: Paganerds (heidnische Klugscheißer), Geisterbegeisterte, Leute, die Bücher von Hembrick oder Lindqvorn lesen, die sich für Magie, Mythologie, Hexerei interessieren.
Aufgabenstellung
Es sollte wie ein magisches Buch aussehen.
Es wäre schön, auf die in der Einladung erwähnte schwarze Kammer anzuspielen, dort hängt über dem Altar das Luft-Tattwa, ein Kreis in luftig-hellem Blau auf schwarzem Grund.
Ansonsten eine Art Rahmen, vielleicht sowas wie magische Siegel, die das gefährliche Buch unter Kontrolle halten.
Es wäre toll, wenn die Schrift, der Name 'Mira Tolvane' und der Titel 'Vom Nebelreich' im Zusammenhang mit dem hellen Kreis ein passendes kalligraphisches Bild ergeben könnten.
Die angefügten Bilder dienen als Orientierungshilfe.
Falls es nach dem ebook eine Printversion gibt, wäre es schön, auf dem ebook-cover-Design aufzubauen.

```html
<!DOCTYPE html>
<html lang="de">
<head>
<meta charset="utf-8">
<title>Vom Nebelreich – Mira Tolvane</title>
<link rel="stylesheet" href="https://fonts.googleapis.com/css2?family=Germania+One&display=swap">
<style>
  :root {
    --stage: #d9d6d2;
    --cover-top: #1d3550;
    --cover-mid: #152a40;
    --cover-deep: #0c1826;
    --frame: #d8dde2;
    --title: #ececec;
    --portal-ring: #e6ebef;
    --portal-light: #c3def2;
    --portal-deep: #86b3e0;
  }
  * { margin: 0; padding: 0; box-sizing: border-box; }
  html, body {
    width: 1200px;
    height: 960px;
    overflow: hidden;
    background: var(--stage);
  }
  .book-cover {
    position: absolute;
    left: 280px;
    top: 40px;
    width: 640px;
    height: 880px;
    background: radial-gradient(ellipse at 50% 30%, var(--cover-top) 0%, var(--cover-mid) 50%, var(--cover-deep) 100%);
    overflow: hidden;
    font-family: "Germania One", "UnifrakturCook", serif;
  }
  .cover-scene {
    position: absolute;
    inset: 0;
    background:
      linear-gradient(180deg, rgba(40,70,100,0.35) 0%, rgba(20,40,60,0) 35%, rgba(10,25,40,0.25) 70%, rgba(6,14,24,0.7) 100%);
  }
  .cover-frame {
    position: absolute;
    inset: 0;
  }
  .frame-ornament {
    position: absolute;
    width: 44px;
    height: 80px;
    background: linear-gradient(180deg, #1a2f46, #17293e);
    border-radius: 6px;
  }
  .frame-ornament--left { left: 16px; top: 300px; }
  .frame-ornament--right { right: 16px; top: 480px; }
  .cover-title {
    position: absolute;
    left: 0;
    right: 0;
    top: 150px;
    text-align: center;
    color: var(--title);
    font-weight: 400;
    font-size: 104px;
    line-height: 0.9;
    letter-spacing: 2px;
    text-shadow: 3px 4px 6px rgba(0,0,0,0.55);
  }
  .cover-title span { display: block; }
  .air-portal {
    position: absolute;
    left: 170px;
    top: 408px;
    width: 300px;
    height: 300px;
    border-radius: 50%;
    border: 7px solid var(--portal-ring);
    padding: 10px;
  }
  .air-portal::after {
    content: "";
    display: block;
    width: 100%;
    height: 100%;
    border-radius: 50%;
    background: linear-gradient(150deg, var(--portal-light), var(--portal-deep));
  }
  .cover-author {
    position: absolute;
    left: 0;
    right: 0;
    top: 758px;
    text-align: center;
    color: var(--title);
    font-size: 44px;
    letter-spacing: 1px;
    text-shadow: 2px 3px 5px rgba(0,0,0,0.6);
  }
</style>
</head>
<body>
  <main class="book-cover">
    <div class="cover-scene" role="img" aria-label="Dunkle, nebelige Treppe in der schwarzen Kammer mit schemenhafter Gestalt"></div>

    <svg class="cover-frame" width="640" height="880" viewBox="0 0 640 880" aria-hidden="true">
      <path d="M52 26 H588 A26 26 0 0 0 614 52 V828 A26 26 0 0 0 588 854 H52 A26 26 0 0 0 26 828 V52 A26 26 0 0 0 52 26 Z"
            fill="none" stroke="var(--frame)" stroke-width="2"/>
      <path d="M60 38 H580 A22 22 0 0 0 602 60 V820 A22 22 0 0 0 580 842 H60 A22 22 0 0 0 38 820 V60 A22 22 0 0 0 60 38 Z"
            fill="none" stroke="var(--frame)" stroke-width="5"/>
    </svg>

    <div class="frame-ornament frame-ornament--left" role="img" aria-label="Verschnörkeltes Rahmenornament links"></div>
    <div class="frame-ornament frame-ornament--right" role="img" aria-label="Verschnörkeltes Rahmenornament rechts"></div>

    <h1 class="cover-title"><span>Vom</span><span>Nebelreich</span></h1>

    <div class="air-portal" role="img" aria-label="Luft-Tattwa: hellblauer Kreis"></div>

    <p class="cover-author">Mira Tolvane</p>
  </main>
</body>
</html>
```